Label design/Graphic design required to brand wall paints

Would like to design a paint drum label/graphic to brand paint drums. The product is wall paints which come in plastic containers. (Refer attached pics). I have also attached the logo font. The one in the pictures are a bit too plan - need some color and creativity - not something too jazzy. You can change the icons if you wish to for the Low VOC, Washable & Eco Friendly - or keep the same. Need to incorporate the drum size "20 L" or "20 Ltr." at the bottom of the label.Rest of the matter to be incorporated is as per the content in the sample labels provided. Size of the label can be 230 x 230mm W X H.

Target Market(s)

Buildings Houses

Industry/Entity Type

Painting And Decorating

Colors

Designer to choose colors to be used in the design.

Requirements
Must have
• The content on the label samples given. Must maintain the logo font.
Nice to have
• A little more color -not jazzy. Can try giving color accents to the font if it helps.
Should not have
• Should not be cluttered.

```html
<!DOCTYPE html>
<html lang="en">
<head>
<meta charset="utf-8">
<title>Evenhue Paints – 20 Ltr. Drum Label</title>
<link href="https://fonts.googleapis.com/css2?family=Poiret+One&family=Montserrat:wght@700;800&display=swap" rel="stylesheet">
<style>
  :root {
    --page-bg: #ffffff;
    --navy: #243450;
    --slate: #6e7a8f;
    --sky: #2f8fd0;
    --sky-light: #6cb7e6;
    --white: #ffffff;
  }
  * { box-sizing: border-box; margin: 0; padding: 0; }
  html, body {
    width: 1200px; height: 1195px; overflow: hidden;
    background: var(--page-bg);
  }
  .label {
    position: absolute;
    left: 250px; top: 208px;
    width: 700px; height: 780px;
    background: linear-gradient(180deg, var(--navy) 0%, var(--navy) 58%, var(--slate) 88%, var(--slate) 100%);
    overflow: hidden;
  }
  .label__sheen {
    position: absolute; inset: 0; width: 100%; height: 100%;
  }
  .tagline-band {
    position: absolute; left: 0; right: 0; top: 40px; height: 62px;
    background: var(--white);
    border-top: 4px solid var(--sky);
    border-bottom: 4px solid var(--sky);
    display: flex; align-items: center; justify-content: center;
  }
  .tagline-band__text {
    font-family: "Montserrat", sans-serif; font-weight: 800;
    font-size: 27px; letter-spacing: 4px; color: var(--sky);
  }
  .splash {
    position: absolute; left: 20px; top: 200px; width: 660px; height: 390px;
    background: linear-gradient(180deg, var(--sky) 0%, var(--sky-light) 100%);
    border-radius: 30px 60px 40px 80px / 40px 30px 70px 50px;
  }
  .brand-name {
    position: absolute; left: 0; right: 0; top: 330px;
    text-align: center;
    font-family: "Montserrat", sans-serif; font-weight: 700;
    font-size: 64px; letter-spacing: 3px; line-height: 1;
    color: var(--white);
  }
  .subtitle {
    position: absolute; left: 0; right: 0; top: 505px;
    text-align: center;
    font-family: "Poiret One", sans-serif; font-size: 38px; font-weight: 400;
    color: var(--white); letter-spacing: 1px;
  }
  .badges {
    position: absolute; left: 28px; top: 615px;
    display: flex; gap: 18px;
  }
  .badge { width: 94px; height: 94px; }
  .volume {
    position: absolute; right: 40px; top: 615px;
    font-family: "Montserrat", sans-serif; font-weight: 700;
    font-size: 32px; color: var(--white);
  }
</style>
</head>
<body>
  <main class="label">
    <svg class="label__sheen" viewBox="0 0 700 780" aria-hidden="true">
      <path d="M700 150 C520 330 460 560 470 780 L700 780 Z" fill="#243450" opacity="0.55"/>
    </svg>

    <div class="tagline-band">
      <span class="tagline-band__text">A ONE COAT APPLICATION</span>
    </div>

    <div class="splash" role="img" aria-label="Blue brush-stroke paint splash behind the product name"></div>

    <h1 class="brand-name">EVENHUE PAINTS</h1>

    <p class="subtitle">PAINT AND PRIMER IN ONE</p>

    <div class="badges">
      <svg class="badge" viewBox="0 0 94 94" role="img" aria-label="Low VOC formula badge">
        <circle cx="47" cy="47" r="44" fill="none" stroke="#ffffff" stroke-width="3"/>
        <circle cx="47" cy="47" r="28" fill="#243450" stroke="#ffffff" stroke-width="3"/>
      </svg>
      <svg class="badge" viewBox="0 0 94 94" role="img" aria-label="Washable badge">
        <circle cx="47" cy="47" r="44" fill="none" stroke="#ffffff" stroke-width="3"/>
        <circle cx="47" cy="47" r="28" fill="#243450" stroke="#ffffff" stroke-width="3"/>
      </svg>
      <svg class="badge" viewBox="0 0 94 94" role="img" aria-label="Eco friendly badge">
        <circle cx="47" cy="47" r="44" fill="none" stroke="#ffffff" stroke-width="3"/>
        <circle cx="47" cy="47" r="28" fill="#243450" stroke="#ffffff" stroke-width="3"/>
      </svg>
    </div>

    <p class="volume">20 Ltr.</p>
  </main>
</body>
</html>
```